Federal Government IT Reseller - Website Overhaul

We are looking to have the website www.brambleforgetech.com to have a new look and increased functionality.

Brambleforge Technologies is a small US Federal Government IT hardware/software/services Value-added Reseller. Creating content is not the problem, we just need some help overhauling the site and getting some direction on what information should go where.

Short list of competitor's websites for reference:

http://www.kvtechnologies.com/
http://tarvelgov.com/
http://www.pellquay.com/
http://vaultmoth.com/
http://www.quorb7.com/

Short list of technology partner websites for reference:

http://www.zelnix.com/
http://www.purvalo.com/
http://www.dabrun.com/

Target Market(s)

US Federal Government - Bureau of Coastal Mapping and Civilian Agencies.

Large Prime Contractors - Harwell Oskey, Pemberly Atwater, Tavros

IT End Users and Purchasing Departments

Industry/Entity Type

Government

Requirements
Must have
• Social media buttons on homepage and contact us page: WorkLoop, Chatterbox, Quipster.
• News page for blog posts/Press releases/etc (comments turned off).
• Brambleforge Logo, Green/Plum color scheme, please see attached files for reference.
• A more functional Solutions page that is easier to digest and look at. We have many more solutions that we'd like to display but this was the best we could do for a one page mock up. Some expansion buttons for each header would be excellent.
Nice to have
• A more functional contact us page. We have more content (2nd office location, additional e-mail addresses, etc) - but we know how to use Wordpress, just looking for something new to work off of.
• A functional support page, we plan on using a HelpNook form on the support page.
• A more functional Clients page that can appropriately incorporate references and highlight large contracts/contract vehicles that Brambleforge Technologies has been awarded.

```html
<!DOCTYPE html>
<html lang="en">
<head>
<meta charset="utf-8">
<title>Brambleforge Technologies</title>
<link href="https://fonts.googleapis.com/css2?family=Michroma&family=Arimo:wght@400;700&family=Open+Sans:wght@400;600;700&display=swap" rel="stylesheet">
<style>
:root{
  --black:#0a0a0a;
  --green:#8dc13c;
  --plum:#6b2d5c;
  --text:#1b1b1b;
  --muted:#5a5a5a;
  --hero:#e6e6e6;
  --card:#f4f4f2;
  --footer:#2b2b2b;
  --footer-line:#444;
  --quote:#9cc24e;
}
*{box-sizing:border-box;margin:0;padding:0}
html,body{width:758px;height:1200px;overflow:hidden}
body{position:relative;background:#fff;font-family:"Arimo",Arial,sans-serif;color:var(--text);font-size:8px}
.abs{position:absolute}
.topbar{left:0;top:0;width:758px;height:28px;background:var(--black);color:#fff;font-size:8.5px}
.topbar span{position:absolute;top:9px}
.header{left:0;top:28px;width:758px;height:80px;background:#fff}
.brand{left:62px;top:63px;font-family:"Arimo",sans-serif;font-weight:700;font-size:14px;color:#2a2a2a;display:flex;align-items:center;gap:5px;white-space:nowrap}
.brand i{display:block;width:10px;height:10px;border-radius:50%;background:var(--plum)}
.tagline{left:184px;top:52px;font-family:"Courier New",monospace;font-style:italic;font-size:6.8px;letter-spacing:1px;color:#666;line-height:10.5px}
.nav{left:318px;top:57px;display:flex}
.nav div{text-align:center;margin-right:22px}
.nav b{display:block;font-size:9.5px;color:#111}
.nav small{font-size:7px;color:#222}
.hero{left:0;top:108px;width:758px;height:310px;background:var(--hero)}
.hero h1{position:absolute;left:62px;top:52px;font-family:"Michroma",sans-serif;font-weight:700;font-size:17px;letter-spacing:.5px}
.hero p{position:absolute;left:62px;top:83px;width:270px;font-size:8px;line-height:14px}
.features{left:62px;top:233px;width:262px;height:82px;background:#111;border:3px solid var(--green);border-left:none}
.features .tab{position:absolute;left:0;top:0;width:20px;height:100%;background:var(--green)}
.features .tab span{position:absolute;left:3px;top:70px;transform:rotate(-90deg);transform-origin:left top;font-family:"Open Sans",sans-serif;font-weight:700;font-size:9px;color:#111;white-space:nowrap}
.feat{position:absolute;color:#fff;font-weight:700;font-size:8px;display:flex;align-items:center;gap:10px}
.feat i{display:block;width:18px;height:14px;border-radius:3px;background:#bbb}
.server{left:400px;top:124px;width:232px;height:192px;background:linear-gradient(#2a3540,#0c1015);border-radius:4px}
h2.sec{font-family:"Michroma",sans-serif;font-weight:700;font-size:11.5px;color:#111}
.card{width:142px;height:150px;background:var(--card);border-left:2px solid var(--green);border-right:2px solid var(--green);border-bottom:2px solid var(--green);border-top:1px solid #ddd;box-shadow:0 1px 3px rgba(0,0,0,.08)}
.card .ic{position:absolute;left:34px;top:15px;width:30px;height:30px}
.card h3{position:absolute;left:13px;top:64px;font-size:7px;font-weight:700}
.card p{position:absolute;left:13px;top:74px;width:124px;font-size:6.9px;line-height:10.2px;color:#333}
.card a{position:absolute;left:13px;top:113px;font-size:7.5px;color:#222;text-decoration:none}
.adv p{font-size:8px;line-height:12.6px;color:#111;margin-bottom:12px;width:180px}
.adv ul{list-style:none;font-family:"Open Sans",sans-serif;font-size:8.6px;color:#555}
.adv li{height:16.5px;display:flex;align-items:center;gap:11px;padding-left:4px}
.adv li i{display:block;width:9px;height:9px;border-radius:2px}
.divider{left:62px;top:836px;width:631px;height:1px;background:#ddd}
.clients-title{left:0;top:851px;width:758px;text-align:center;font-family:"Michroma",sans-serif;font-weight:700;font-size:11.5px}
.clients-intro{left:66px;top:869px;width:625px;font-size:8px;line-height:14px;color:var(--muted)}
.quote{width:238px;height:88px;background:#eeeee8}
.quote p{position:absolute;left:20px;top:20px;width:200px;text-align:center;color:var(--quote);font-size:7px;line-height:9.4px;letter-spacing:.2px}
.quote b{position:absolute;left:28px;top:71px;font-weight:400;font-size:8.5px;color:#111}
.quote .mark{position:absolute;right:4px;bottom:4px;width:14px;height:10px;border-radius:5px;background:var(--plum);opacity:.55}
.avatar{width:80px;height:80px;border-radius:50%;background:radial-gradient(circle at 50% 40%,#c9d6e3,#6d86a3)}
.footer{left:0;top:1022px;width:758px;height:160px;background:var(--footer);color:#fff}
.fcol{position:absolute;top:10px}
.fcol h4{font-family:"Open Sans",sans-serif;font-weight:600;font-size:10.5px;margin-bottom:8px;white-space:nowrap}
.fcol ul{list-style:none;font-size:7.6px}
.fcol li{height:14px;display:flex;align-items:center;gap:8px;font-weight:700}
.fsep{position:absolute;top:15px;width:1px;height:138px;background:var(--footer-line)}
.news p{font-size:7.4px;line-height:11.5px;font-weight:700;width:200px}
.search{position:absolute;left:2px;top:59px;width:188px;height:24px;background:#555;border-radius:2px}
.search .btn{position:absolute;right:0;top:0;width:32px;height:24px;background:var(--green);border-right:2px solid var(--plum)}
.social{position:absolute;left:4px;top:106px;display:flex;gap:10px;font-family:"Open Sans",sans-serif;font-weight:700;font-size:8.5px;color:var(--green);white-space:nowrap}
.copyright{left:0;top:1182px;width:758px;height:18px;background:#111;color:#fff;font-size:6.8px;text-align:center;line-height:18px}
</style>
</head>
<body>

<div class="abs topbar">
  <span style="left:62px">
    <svg width="7" height="8" viewBox="0 0 10 10" style="vertical-align:-1px"><path d="M2 0l2 3-1 1c1 2 2 3 3 3l1-1 3 2-1 2C4 10 0 6 0 2z" fill="#8dc13c"/></svg>
    Call us: 1-800-555-0190</span>
  <span style="left:186px">
    <svg width="10" height="8" viewBox="0 0 12 10" style="vertical-align:-1px"><ellipse cx="6" cy="4.5" rx="5.5" ry="4.2" fill="#8dc13c"/><path d="M2 7l-1 3 4-2z" fill="#8dc13c"/></svg>
    Live support</span>
  <span style="left:624px">
    <svg width="11" height="8" viewBox="0 0 12 9" style="vertical-align:-1px"><circle cx="4" cy="2.5" r="2.2" fill="#8dc13c"/><circle cx="8.5" cy="3" r="2" fill="#8dc13c"/><path d="M0 9c0-3 2-4 4-4s4 1 4 4zM6 9c1-3 2-3.5 3-3.5s3 1 3 3.5z" fill="#8dc13c"/></svg>
    Clients Login</span>
</div>

<div class="abs header"></div>
<div class="abs brand"><i></i>Brambleforge</div>
<div class="abs tagline">AN IT VALUE-ADDED<br>RESELLER TO THE<br>U.S. GOVERNMENT<br>AND ITS INTEGRATORS</div>
<nav class="abs nav">
  <div><b>Home</b><small>Welcome</small></div>
  <div><b>Solutions</b><small>plans</small></div>
  <div><b>Clients</b><small>info</small></div>
  <div><b>Company</b><small>its technologies</small></div>
  <div><b>Events</b><small>IT articles</small></div>
  <div style="margin-right:0"><b>Contact</b><small>and quotes</small></div>
</nav>

<section class="abs hero">
  <h1>Lorem ipsum dolor sit amet</h1>
  <p>adipisi cing elit. Ab expedita sintpaa accusamus impedit repellendus amit assumenda quo facilis modi sunt poro!</p>
</section>
<svg class="abs" style="left:0;top:355px" width="758" height="65" viewBox="0 355 758 65">
  <path d="M0 355H758V364L360 395L0 364Z" fill="#e6e6e6"/>
  <path d="M0 364L360 395L758 364V380L360 408L0 380Z" fill="#8dc13c"/>
  <path d="M0 380L360 408L758 380V385L360 413L0 385Z" fill="#111"/>
  <path d="M0 385L360 413L758 385V420H0Z" fill="#fff"/>
</svg>

<div class="abs features">
  <div class="tab"><span>Features</span></div>
  <div class="feat" style="left:36px;top:18px"><i></i>quo facilis</div>
  <div class="feat" style="left:146px;top:16px"><i style="border-radius:50%;width:18px;height:18px;background:#7f93a3"></i>repellendus</div>
  <div class="feat" style="left:36px;top:53px"><i style="background:#aaa"></i>Ab expedita</div>
  <div class="feat" style="left:146px;top:53px"><i style="background:#ddd"></i>Ipsam eos iste</div>
</div>

<div class="abs server" role="img" aria-label="Three dark server towers with blue glowing stripes"></div>

<h2 class="abs sec" style="left:62px;top:436px">Lorem ipsum dolor sit amet</h2>

<div class="abs card" style="left:62px;top:462px">
  <div class="ic" role="img" aria-label="Pink globe icon" style="border-radius:50%;background:radial-gradient(circle at 40% 35%,#f2a2d4,#b0196f)"></div>
  <h3>Lorem ipsum</h3>
  <p>Fairs and festivals capture the flavor of Idaho communities, with a variety occurring throughout.</p>
  <a>More info [+]</a>
</div>
<div class="abs card" style="left:286px;top:462px">
  <div class="ic" role="img" aria-label="Server rack icon" style="left:50px;width:30px;background:linear-gradient(90deg,#333,#777,#333)"></div>
  <h3 style="top:58px">Lorem ipsum</h3>
  <p style="top:68px">Fairs and festivals capture the flavor of Idaho communities, with a variety occurring throughout.</p>
  <a style="top:105px">More info [+]</a>
</div>
<div class="abs card" style="left:62px;top:654px">
  <div class="ic" role="img" aria-label="Wrench and screwdriver icon" style="left:42px;background:linear-gradient(135deg,#ccc 45%,#c8202a 55%);border-radius:4px"></div>
  <h3>Lorem ipsum</h3>
  <p>Fairs and festivals capture the flavor of Idaho communities, with a variety occurring throughout.</p>
  <a>More info [+]</a>
</div>
<div class="abs card" style="left:286px;top:654px">
  <svg class="ic" style="left:50px" viewBox="0 0 30 30">
    <circle cx="15" cy="15" r="14" fill="#2a63c4"/>
    <path d="M15 15V1A14 14 0 0 1 29 15Z" fill="#7bc043"/>
    <path d="M15 15H29A14 14 0 0 1 24 25.7Z" fill="#f2a12a"/>
  </svg>
  <h3 style="top:58px">Lorem ipsum</h3>
  <p style="top:68px">Fairs and festivals capture the flavor of Idaho communities, with a variety occurring throughout.</p>
  <a style="top:105px">More info [+]</a>
</div>

<h2 class="abs sec" style="left:508px;top:436px">Advanced Technology</h2>
<div class="abs adv" style="left:508px;top:452px">
  <p>Lorem ipsum dolor sit amet, consectu adipisi cing elit. Ab expedita sintpara accusamus impedit repellendus amit assumenda quo facilis modi sunt poro!</p>
  <p>Ab expedita sintpara accusamus impedit repellendus amit assumenda quo facilis modi sunt poro!</p>
  <ul>
    <li><i style="background:#e0b12c"></i>Highest security rate</li>
    <li><i style="background:#7bb32e;border-radius:50%"></i>24/7 Live Support</li>
    <li><i style="background:#d33"></i>Easy website builder</li>
    <li><i style="background:#3a6fa8"></i>Pocketphone control Panel</li>
    <li><i style="background:#f0a830"></i>Dedicated FTP software</li>
    <li><i style="background:#c33;border-radius:50%"></i>Free domain names</li>
    <li><i style="background:#999"></i>Various disk spaces</li>
    <li><i style="background:#b51c1c"></i>E-commerce solutions</li>
    <li><i style="background:#aaa"></i>KeelSQL &amp; PostwardSQL Databases</li>
    <li><i style="background:#3c7fb5"></i>Powerfull HostDeck</li>
    <li><i style="background:#555;border-radius:50%"></i>Unlimited bandwidth</li>
  </ul>
  <p style="margin-top:12px;font-size:8.5px;color:#222">More info [+]</p>
</div>

<div class="abs divider"></div>
<div class="abs clients-title">what Our Clients are saying</div>
<p class="abs clients-intro">We are providing hosting services since 2006. In the past few years many small and large companies have trusted us to help their companies to grow in the Web World. Here is just a sample of what they have to say about services we provide.</p>

<div class="abs quote" style="left:120px;top:916px">
  <p>Lorem Ipsum has been the industry's standard dummy text ever since the 1500s, when an unknown printer took a galley of type and scram The Service here is great. I would highly recommend it solutions to anybody wanting</p>
  <b>- John Doe, Awesome Inc</b>
  <span class="mark"></span>
</div>
<div class="abs avatar" style="left:62px;top:920px" role="img" aria-label="Portrait photo of a smiling man in a suit"></div>
<div class="abs quote" style="left:455px;top:916px">
  <p>Lorem Ipsum has been the industry's standard dummy text ever since the 1500s, when an unknown printer took a galley of type and scram The Service here is great. I would highly recommend it solutions to anybody wanting</p>
  <b>- Stella, Awesome Inc</b>
  <span class="mark"></span>
</div>
<div class="abs avatar" style="left:396px;top:920px" role="img" aria-label="Portrait photo of a smiling businesswoman"></div>

<footer class="abs footer">
  <div class="fcol" style="left:78px"><h4>About Brambleforge</h4>
    <ul>
      <li><svg width="8" height="7" viewBox="0 0 8 7"><path d="M0 4l3 3 5-7" stroke="#8dc13c" stroke-width="1.6" fill="none"/></svg>Thailand</li>
      <li><svg width="8" height="7" viewBox="0 0 8 7"><path d="M0 4l3 3 5-7" stroke="#8dc13c" stroke-width="1.6" fill="none"/></svg>Indonesia</li>
      <li><svg width="8" height="7" viewBox="0 0 8 7"><path d="M0 4l3 3 5-7" stroke="#8dc13c" stroke-width="1.6" fill="none"/></svg>Laos</li>
      <li><svg width="8" height="7" viewBox="0 0 8 7"><path d="M0 4l3 3 5-7" stroke="#8dc13c" stroke-width="1.6" fill="none"/></svg>Cambodia</li>
      <li><svg width="8" height="7" viewBox="0 0 8 7"><path d="M0 4l3 3 5-7" stroke="#8dc13c" stroke-width="1.6" fill="none"/></svg>Japan</li>
      <li><svg width="8" height="7" viewBox="0 0 8 7"><path d="M0 4l3 3 5-7" stroke="#8dc13c" stroke-width="1.6" fill="none"/></svg>Myanmar</li>
      <li><svg width="8" height="7" viewBox="0 0 8 7"><path d="M0 4l3 3 5-7" stroke="#8dc13c" stroke-width="1.6" fill="none"/></svg>Vietnam</li>
      <li><svg width="8" height="7" viewBox="0 0 8 7"><path d="M0 4l3 3 5-7" stroke="#8dc13c" stroke-width="1.6" fill="none"/></svg>China</li>
    </ul></div>
  <div class="fsep" style="left:192px"></div>
  <div class="fcol" style="left:210px"><h4>Resources</h4>
    <ul>
      <li><svg width="8" height="7" viewBox="0 0 8 7"><path d="M0 4l3 3 5-7" stroke="#8dc13c" stroke-width="1.6" fill="none"/></svg>Demo</li>
      <li><svg width="8" height="7" viewBox="0 0 8 7"><path d="M0 4l3 3 5-7" stroke="#8dc13c" stroke-width="1.6" fill="none"/></svg>Technical</li>
      <li><svg width="8" height="7" viewBox="0 0 8 7"><path d="M0 4l3 3 5-7" stroke="#8dc13c" stroke-width="1.6" fill="none"/></svg>Support</li>
      <li><svg width="8" height="7" viewBox="0 0 8 7"><path d="M0 4l3 3 5-7" stroke="#8dc13c" stroke-width="1.6" fill="none"/></svg>Merchant's</li>
      <li><svg width="8" height="7" viewBox="0 0 8 7"><path d="M0 4l3 3 5-7" stroke="#8dc13c" stroke-width="1.6" fill="none"/></svg>Guide</li>
      <li><svg width="8" height="7" viewBox="0 0 8 7"><path d="M0 4l3 3 5-7" stroke="#8dc13c" stroke-width="1.6" fill="none"/></svg>Developer's</li>
      <li><svg width="8" height="7" viewBox="0 0 8 7"><path d="M0 4l3 3 5-7" stroke="#8dc13c" stroke-width="1.6" fill="none"/></svg>Guide</li>
      <li><svg width="8" height="7" viewBox="0 0 8 7"><path d="M0 4l3 3 5-7" stroke="#8dc13c" stroke-width="1.6" fill="none"/></svg>Add-ons</li>
    </ul></div>
  <div class="fsep" style="left:308px"></div>
  <div class="fcol" style="left:352px"><h4>Quick Links</h4>
    <ul>
      <li><svg width="8" height="7" viewBox="0 0 8 7"><path d="M0 4l3 3 5-7" stroke="#8dc13c" stroke-width="1.6" fill="none"/></svg>Home</li>
      <li><svg width="8" height="7" viewBox="0 0 8 7"><path d="M0 4l3 3 5-7" stroke="#8dc13c" stroke-width="1.6" fill="none"/></svg>Destinations</li>
      <li><svg width="8" height="7" viewBox="0 0 8 7"><path d="M0 4l3 3 5-7" stroke="#8dc13c" stroke-width="1.6" fill="none"/></svg>Tours</li>
      <li><svg width="8" height="7" viewBox="0 0 8 7"><path d="M0 4l3 3 5-7" stroke="#8dc13c" stroke-width="1.6" fill="none"/></svg>Holiday Types</li>
      <li><svg width="8" height="7" viewBox="0 0 8 7"><path d="M0 4l3 3 5-7" stroke="#8dc13c" stroke-width="1.6" fill="none"/></svg>Best Value</li>
      <li><svg width="8" height="7" viewBox="0 0 8 7"><path d="M0 4l3 3 5-7" stroke="#8dc13c" stroke-width="1.6" fill="none"/></svg>About Us</li>
      <li><svg width="8" height="7" viewBox="0 0 8 7"><path d="M0 4l3 3 5-7" stroke="#8dc13c" stroke-width="1.6" fill="none"/></svg>Blog</li>
    </ul></div>
  <div class="fsep" style="left:455px"></div>
  <div class="fcol news" style="left:477px;top:8px"><h4>Join Our Newsletter</h4>
    <p>Stay up to date with all our latest tips to improve your websites performance with our newsletter.</p>
    <div class="search"><div class="btn">
      <svg width="30" height="24" viewBox="0 0 30 24"><circle cx="13" cy="10" r="5" stroke="#fff" stroke-width="2" fill="none"/><path d="M17 14l5 5" stroke="#fff" stroke-width="3"/></svg>
    </div></div>
    <div class="social"><span>Quipster</span><span>Chatterbox</span><span>Circlecast</span><span>WorkLoop</span></div>
  </div>
</footer>
<div class="abs copyright">Copyright © 2013 brambleforge. All rights reserved.</div>

</body>
</html>
```